Website design for Maple Nook Kidcare

I need a website designed for my daycare business, Maple Nook Kidcare, now that I have a new logo. My former website was ok but simple and I did not have a logo yet. It also was created by me using a template and was entirely pink. I loved the bright, happy feel of it but worried it might not appeal as much to potential clients who have sons. Therefore, I need a site which will appeal to both genders while still keeping the cheerful color scheme of my new logo, which has pinks, blue, green and cream.

Reason: Hello! I am still trying to download my new logo and am sorry it is taking me so long. Hopefully I will it posted by the end of today (US Eastern Standard Time). Thank you all very much for your patience!

Hello! I have finally managed to upload my new logo for you to use in designing my website. I'm sorry it took so long and greatly appreciate your time and creative efforts! I look forward to seeing what is submitted based on my logo design and its style/colors.

Many thanks!

Reason: As I've been traveling and posted my logo file late, I am extending my deadline. I am now back and can focus on providing more and better feedback. I appreciate your patience and submissions very much!

Reason: I need more time to provide feedback and make decisions.

Industry/Entity Type

Daycare

Colors
0192cd
33a6d7
86cae7
cadf82
fbf289
add136
e34197

```html
<!DOCTYPE html>
<html lang="en">
<head>
<meta charset="utf-8">
<title>Maple Nook Kidcare</title>
<link href="https://fonts.googleapis.com/css2?family=Sniglet:wght@400;800&family=Open+Sans:wght@400;600;700&display=swap" rel="stylesheet">
<style>
  :root{
    --blue-deep:#0192cd;
    --blue:#33a6d7;
    --blue-soft:#86cae7;
    --green-soft:#cadf82;
    --yellow:#fbf289;
    --green:#add136;
    --pink:#e34197;
    --pink-soft:#f3a9cf;
    --cream:#fffdf3;
    --text:#6d6d6d;
    --line:#d9d9d9;
  }
  *{box-sizing:border-box;margin:0;padding:0}
  html,body{width:804px;height:1200px;overflow:hidden}
  body{position:relative;background:#fff;font-family:"Open Sans",sans-serif;color:var(--text)}
  .abs{position:absolute}

  /* header */
  .brand{left:72px;top:24px;display:flex;align-items:center;gap:10px}
  .brand-dot{width:40px;height:40px;border-radius:50%;background:var(--pink)}
  .brand-name{font-family:"Sniglet",sans-serif;font-size:27px;color:var(--pink);line-height:1}
  .contact-box{right:74px;top:22px;width:122px;height:40px;border-radius:6px;background:var(--green-soft);
    display:flex;align-items:center;gap:6px;padding:0 8px}
  .contact-box svg{flex:none}
  .contact-lines{font-size:8px;line-height:13px;color:#4e5a2a;font-weight:600}

  /* navigation */
  .main-nav{left:0;top:96px;width:804px;height:22px;background:var(--green-soft);
    display:flex;justify-content:center;gap:16px;align-items:center}
  .main-nav a{font-size:8px;font-weight:700;color:#fff;text-decoration:none}
  .main-nav a.current{color:var(--pink)}

  /* hero */
  .hero{left:75px;top:124px;width:654px;height:238px;overflow:hidden;border-radius:2px}
  .hero-photo{width:100%;height:100%;background:linear-gradient(120deg,#b9895d 0%,#e3c7a1 35%,#c0523f 60%,#5b6f7c 100%)}
  .hero-caption{left:10px;bottom:12px;width:300px;font-size:8px;line-height:12px;color:#fff;
    background:rgba(0,0,0,.25);padding:5px 7px}
  .slide-arrows{right:12px;bottom:14px;display:flex;gap:5px}
  .arrow{width:16px;height:16px;border-radius:50%;background:#fff;display:flex;align-items:center;justify-content:center}

  /* welcome */
  .welcome-title{left:0;top:378px;width:804px;text-align:center;font-family:"Sniglet",sans-serif;
    font-size:19px;line-height:22px;color:var(--pink)}
  .welcome-copy{left:100px;top:426px;width:604px;text-align:center;font-size:7.5px;line-height:11px}

  /* feature cards */
  .card{top:478px;width:180px;height:138px;border-radius:4px;text-align:center;padding-top:14px}
  .card .badge{width:40px;height:40px;border-radius:50%;background:#fff;margin:0 auto 6px;
    display:flex;align-items:center;justify-content:center}
  .card h3{font-family:"Sniglet",sans-serif;font-size:15px;font-weight:400;color:#fff}
  .card p{font-size:7px;line-height:10px;color:#fff;margin:6px 14px 0}
  .card-learning{left:88px;background:var(--blue-soft)}
  .card-creativity{left:313px;background:var(--green-soft)}
  .card-sharing{left:536px;background:var(--pink-soft)}

  /* news & testimonials */
  .block-title{top:638px;display:flex;align-items:center;gap:6px;font-family:"Sniglet",sans-serif;color:var(--pink)}
  .block-title::after{content:"";height:1px;background:var(--line);flex:1}
  .news-title{left:75px;width:190px;font-size:13px}
  .testi-title{left:285px;width:444px;font-size:16px}
  .news-copy{left:75px;top:660px;width:190px;font-size:7px;line-height:10px}
  .testi-copy{left:285px;top:660px;width:444px;font-size:7px;line-height:10px}
  .block-arrows{right:75px;top:718px;display:flex;gap:5px}
  .block-arrows .arrow{background:var(--pink)}

  /* footer */
  .site-footer{left:0;top:755px;width:804px;height:172px;background:linear-gradient(#9fd5ee,var(--blue-soft))}
  .footer-col{top:18px;color:#fff}
  .footer-col h4{font-family:"Sniglet",sans-serif;font-weight:400;font-size:13px;margin-bottom:8px}
  .footer-col ul{list-style:none;font-size:8px;line-height:14px}
  .footer-col li::before{content:"› "}
  .nav-col{left:112px}
  .nav-col .lists{display:flex;gap:30px}
  .social-col{left:330px}
  .socials{display:flex;gap:6px}
  .socials span{width:22px;height:22px;border-radius:50%;background:#fff;opacity:.9}
  .location-col{left:560px}
  .location-col .pin{display:flex;gap:8px;align-items:flex-start}
  .location-col p{font-size:8px;line-height:12px}

  /* scenery */
  .scenery{left:0;top:927px;width:804px;height:273px;
    background:linear-gradient(180deg,var(--cream) 0%,#f4f8e4 55%,var(--green) 88%,#8cb62a 100%)}
</style>
</head>
<body>

<header>
  <div class="abs brand">
    <span class="brand-dot"></span>
    <span class="brand-name">Maple Nook Kidcare</span>
  </div>
  <div class="abs contact-box">
    <svg width="12" height="12" viewBox="0 0 24 24"><path fill="#4e5a2a" d="M6.6 10.8a15.1 15.1 0 0 0 6.6 6.6l2.2-2.2c.3-.3.7-.4 1-.2 1.1.4 2.3.6 3.6.6.6 0 1 .4 1 1V20c0 .6-.4 1-1 1A17 17 0 0 1 3 4c0-.6.4-1 1-1h3.5c.6 0 1 .4 1 1 0 1.3.2 2.5.6 3.6.1.3 0 .7-.2 1z"/></svg>
    <div class="contact-lines">(555) 014-2287<br>hello@maplenook.example</div>
  </div>
</header>

<nav class="abs main-nav">
  <a class="current" href="#">Home</a><a href="#">About Us</a><a href="#">Programs</a><a href="#">Meet &amp; Greet</a>
  <a href="#">Photos</a><a href="#">Contact Us</a><a href="#">Enrollment</a><a href="#">Parent Log-in</a>
</nav>

<section class="abs hero">
  <div class="hero-photo" role="img" aria-label="Photo of smiling children playing together in a bright classroom"></div>
  <p class="abs hero-caption">Little ones learn, laugh and grow in a warm, safe room filled with toys, books and friends who make every single day feel like a new adventure.</p>
  <div class="abs slide-arrows">
    <span class="arrow"><svg width="8" height="8" viewBox="0 0 10 10"><path d="M7 1 3 5l4 4" stroke="#888" stroke-width="2" fill="none"/></svg></span>
    <span class="arrow"><svg width="8" height="8" viewBox="0 0 10 10"><path d="m3 1 4 4-4 4" stroke="#888" stroke-width="2" fill="none"/></svg></span>
  </div>
</section>

<h1 class="abs welcome-title">Welcome to Maple Nook Kidcare, a playspace<br>where children can play, create, and imagine!</h1>
<p class="abs welcome-copy">Welcome to Maple Nook Kidcare, a licensed home daycare set on a quiet tree-lined street in a friendly neighborhood. We care for a small group of children, from infants to preschoolers, with a gentle daily rhythm of free play, stories, crafts, music, outdoor time and healthy meals. Our cozy rooms are made to help every child feel at home, make friends and grow with confidence.</p>

<section class="abs card card-learning">
  <div class="badge"><svg width="20" height="20" viewBox="0 0 24 24"><path d="M3 5h8v14H3zM13 5h8v14h-8z" fill="var(--blue-soft)"/></svg></div>
  <h3>Learning</h3>
  <p>Hands-on play, picture books and simple games help young minds explore letters, numbers and the world.</p>
</section>
<section class="abs card card-creativity">
  <div class="badge"><svg width="20" height="20" viewBox="0 0 24 24"><circle cx="12" cy="12" r="8" fill="var(--green-soft)"/></svg></div>
  <h3>Creativity</h3>
  <p>Paint, clay, songs and pretend play give every child a joyful way to express big ideas.</p>
</section>
<section class="abs card card-sharing">
  <div class="badge"><svg width="20" height="20" viewBox="0 0 24 24"><path d="M12 20s-8-5-8-10a4 4 0 0 1 8-1 4 4 0 0 1 8 1c0 5-8 10-8 10z" fill="var(--pink-soft)"/></svg></div>
  <h3>Sharing</h3>
  <p>Group games and circle time teach kindness, patience and taking turns with good friends.</p>
</section>

<h2 class="abs block-title news-title">News</h2>
<p class="abs news-copy">Our spring garden project starts next week. Families are welcome to bring seeds and join us for planting morning on Friday.</p>
<h2 class="abs block-title testi-title">Testimonials</h2>
<p class="abs testi-copy">"Our daughter runs through the door every morning with a smile. The care, patience and fun she finds here have helped her grow so much this year, and we feel truly lucky to be part of this little family." — A happy parent</p>
<div class="abs block-arrows">
  <span class="arrow"><svg width="8" height="8" viewBox="0 0 10 10"><path d="M7 1 3 5l4 4" stroke="#fff" stroke-width="2" fill="none"/></svg></span>
  <span class="arrow"><svg width="8" height="8" viewBox="0 0 10 10"><path d="m3 1 4 4-4 4" stroke="#fff" stroke-width="2" fill="none"/></svg></span>
</div>

<footer class="abs site-footer">
  <div class="abs footer-col nav-col">
    <h4>Navigation</h4>
    <div class="lists">
      <ul><li>Home</li><li>About Us</li><li>Services</li><li>Meet &amp; Greet</li></ul>
      <ul><li>Photos</li><li>Contact Us</li><li>Enrollment</li></ul>
    </div>
  </div>
  <div class="abs footer-col social-col">
    <h4>Get social with us</h4>
    <div class="socials"><span></span><span></span><span></span></div>
  </div>
  <div class="abs footer-col location-col">
    <h4>Our Location</h4>
    <div class="pin">
      <svg width="14" height="18" viewBox="0 0 14 18"><path d="M7 0a7 7 0 0 0-7 7c0 5 7 11 7 11s7-6 7-11a7 7 0 0 0-7-7z" fill="#fff"/><circle cx="7" cy="7" r="2.5" fill="var(--blue-soft)"/></svg>
      <p>Maple Nook Kidcare<br>42 Birch Lane<br>Cedarville<br>(555) 014-2287<br>hello@maplenook.example</p>
    </div>
  </div>
</footer>

<div class="abs scenery" role="img" aria-label="Cheerful illustration of grass, flowers, a round tree and buzzing bees along the bottom of the page"></div>

</body>
</html>
```